Sam Greenfield Billboard

**Task Description: Billboard Design for Self Storage Facility**

**Objective:**
Design a captivating billboard to promote our self-storage facility with a focus on our convenient location and online rental capabilities.

**Key Messages to Include:**
1. **Location Emphasis:** Highlight that our facility is located right beside the billboard (maybe by using an arrow pointing left).
2. **Online Rental Convenience:** Feature prominently that customers can "Rent Online Anytime!” or that we are "Always Open Online!"

**Target Audience:**
- Local residents looking for convenient self-storage solutions.
- Businesses needing storage space accessible around the clock.

**Design Elements:**
1. **Visual Impact:** Eye-catching graphics and colors that stand out against the surroundings.
2. **Clear Text:** Bold and concise messaging that can be read and understood quickly.
3. **Contact Information:** Include our phone number and website URL for easy access to further information.

**Additional Information:**
- Billboard dimensions: 12 ft. x 24 ft.
- Preferred color scheme: Bright and attention-grabbing, but professional.
- Branding: Incorporate our logo and brand colors to maintain consistency.

**Deliverables:**
- High-resolution digital file compatible with billboard printing specifications.
- Consider mockups or visualizations for presentation purposes.

Please note that I have attached current logos/graphics that we would love to incorporate into the billboard as well as a picture of our current billboard. Our logo (Sam Greenfield Self Storage - SG navy.png) MUST be incorporated into the billboard. Also feel free to add any of the current descriptions from the picture of our current billboard into the design. Instead of using "Climate Controlled" use "Temperature Controlled". Thank you for your attention to these details. We look forward to reviewing your proposed design!

```html
<!DOCTYPE html>
<html lang="en">
<head>
<meta charset="utf-8">
<title>Sam Greenfield Self Storage – Billboard</title>
<link href="https://fonts.googleapis.com/css2?family=Oswald:wght@500;600&family=Montserrat:wght@500&display=swap" rel="stylesheet">
<style>
  :root {
    --navy: #0f2459;
    --tan: #9a7b5c;
    --white: #ffffff;
    --page: #e9ebee;
    --sky: #3fa3d6;
    --door: #2f8173;
    --lot: #c9c6c0;
  }
  html, body {
    margin: 0;
    width: 994px;
    height: 1200px;
    overflow: hidden;
    background: var(--page);
  }
  .billboard {
    position: absolute;
    left: 27px;
    top: 365px;
    width: 940px;
    height: 470px;
    display: block;
  }
  .headline { font-family: "Oswald", "Arial Narrow", sans-serif; font-weight: 600; fill: var(--white); }
  .brand-name { font-family: "Oswald", "Arial Narrow", sans-serif; font-weight: 600; fill: var(--navy); }
  .address { font-family: "Oswald", "Arial Narrow", sans-serif; font-weight: 600; fill: var(--white); }
  .cta { font-family: "Oswald", "Arial Narrow", sans-serif; font-weight: 500; fill: var(--white); }
  .contact { font-family: "Montserrat", Arial, sans-serif; font-weight: 500; fill: var(--white); }
</style>
</head>
<body>
<svg class="billboard" viewBox="0 0 1143 572" xmlns="http://www.w3.org/2000/svg">
  <defs>
    <linearGradient id="facility-tones" x1="0" y1="0" x2="0" y2="1">
      <stop offset="0" stop-color="#ffffff"/>
      <stop offset="0.26" stop-color="#ffffff"/>
      <stop offset="0.34" stop-color="var(--sky)"/>
      <stop offset="0.45" stop-color="#8fb9b4"/>
      <stop offset="0.6" stop-color="var(--door)"/>
      <stop offset="0.78" stop-color="#6c9890"/>
      <stop offset="0.86" stop-color="var(--lot)"/>
      <stop offset="1" stop-color="#b8b4ad"/>
    </linearGradient>
    <linearGradient id="screen-tones" x1="0" y1="0" x2="0" y2="1">
      <stop offset="0" stop-color="#f2f3f5"/>
      <stop offset="0.35" stop-color="#6b7078"/>
      <stop offset="0.7" stop-color="#d9dce0"/>
      <stop offset="1" stop-color="#f5f6f7"/>
    </linearGradient>
  </defs>

  <!-- background facility photo area -->
  <rect class="facility-photo" x="0" y="0" width="1143" height="572" fill="url(#facility-tones)" role="img" aria-label="Photo of self storage buildings with green roll-up doors under a blue sky"/>

  <!-- navy message panel with tan edges -->
  <polygon class="panel-edge" points="418,0 1133,0 995,572 275,572" fill="var(--tan)"/>
  <polygon class="message-panel" points="435,0 1118,0 980,572 292,572" fill="var(--navy)"/>

  <!-- brand name -->
  <text class="brand-name" x="205" y="98" font-size="44" text-anchor="middle" letter-spacing="1">SAM GREENFIELD</text>
  <text class="brand-name" x="205" y="130" font-size="20" text-anchor="middle" letter-spacing="7">SELF STORAGE</text>

  <!-- headline -->
  <g class="headline" text-anchor="middle">
    <text x="719" y="165" font-size="80" textLength="502" lengthAdjust="spacingAndGlyphs">LARGE/SMALL UNITS</text>
    <text x="719" y="238" font-size="64" textLength="500" lengthAdjust="spacingAndGlyphs">TEMPERATURE CONTROLED</text>
    <text x="719" y="312" font-size="64" textLength="502" lengthAdjust="spacingAndGlyphs">COVERED BOAT/RV PARKING</text>
  </g>

  <!-- address arrow -->
  <polygon class="address-arrow" points="52,419 155,350 155,382 635,382 620,456 155,456 155,488" fill="var(--tan)"/>
  <text class="address" x="380" y="448" font-size="60" text-anchor="middle" textLength="388" lengthAdjust="spacingAndGlyphs">214 MEADOWBROOK DRIVE</text>

  <!-- rent online call to action -->
  <rect class="cta-box" x="713" y="371" width="194" height="87" rx="6" fill="none" stroke="var(--white)" stroke-width="4"/>
  <g class="cta" text-anchor="middle" font-size="29">
    <text x="808" y="409">RENT ONLINE</text>
    <text x="808" y="441">ANYTIME!</text>
  </g>

  <!-- devices showing booking site -->
  <rect x="912" y="338" width="168" height="128" rx="6" fill="#1b1d22"/>
  <rect x="917" y="343" width="158" height="118" fill="url(#screen-tones)" role="img" aria-label="Tablet showing the online rental website"/>
  <rect x="892" y="362" width="38" height="104" rx="6" fill="#1b1d22"/>
  <rect x="895" y="368" width="32" height="92" fill="url(#screen-tones)" role="img" aria-label="Phone showing the online rental website"/>

  <!-- contact band -->
  <polygon class="contact-band" points="190,482 1103,482 1088,547 172,547" fill="var(--tan)"/>
  <g class="phone-icon" transform="translate(225,496)" fill="var(--navy)">
    <path d="M6 4 L14 2 L20 13 L15 17 C17 23 21 27 27 29 L31 24 L42 30 L40 38 C28 42 2 20 6 4 Z"/>
    <path d="M26 6 A14 14 0 0 1 38 18" fill="none" stroke="var(--navy)" stroke-width="3"/>
    <path d="M26 0 A20 20 0 0 1 44 18" fill="none" stroke="var(--navy)" stroke-width="3"/>
  </g>
  <text class="contact" x="290" y="532" font-size="42">555-014-2386</text>
  <g class="web-icon" transform="translate(655,512)" fill="none" stroke="var(--navy)" stroke-width="3">
    <circle cx="0" cy="0" r="17"/>
    <ellipse cx="0" cy="0" rx="7" ry="17"/>
    <line x1="-17" y1="0" x2="17" y2="0"/>
    <path d="M8 6 L20 26 L22 16 L30 14 Z" fill="var(--navy)" stroke="none"/>
  </g>
  <text class="contact" x="688" y="526" font-size="30">SamGreenfieldStorage.com</text>
</svg>
</body>
</html>
```